New Business Card Design Project

Use the flyer uploaded and website www.brightoakbuilders.example for inspiration.
List Our Services on Backside of business cards
Marcus Dell
Harborline Renovations Inc.
Licensed General Contractors
555-014-7390

Contact Information for Business Card

Use the flyer uploaded and website www.brightoakbuilders.example for inspiration. List Our Services on Backside of business cards Marcus Dell Harborline Renovations Inc. Licensed General Contractors 555-014-7390

```html
<!DOCTYPE html>
<html lang="en">
<head>
<meta charset="utf-8">
<title>Harborline Renovations – Business Card</title>
<link href="https://fonts.googleapis.com/css2?family=Cinzel:wght@400&family=Open+Sans:wght@400;600;700&display=swap" rel="stylesheet">
<style>
  :root {
    --bg: #6a6b6e;
    --card: #141414;
    --white: #f2f2f2;
    --muted: #d9d9d9;
    --blue: #2f6fc4;
    --red: #e0232a;
  }
  * { box-sizing: border-box; margin: 0; padding: 0; }
  html, body { width: 1200px; height: 781px; overflow: hidden; }
  body {
    background: radial-gradient(ellipse at 50% 45%, #8a8b8e 0%, var(--bg) 70%);
    font-family: "Open Sans", sans-serif;
    color: var(--white);
    display: flex; align-items: center; justify-content: center; gap: 48px;
  }
  .card {
    width: 525px; height: 300px;
    background: var(--card);
    border-radius: 18px;
    position: relative;
    box-shadow: 0 16px 36px rgba(0,0,0,.45);
  }
  .brand {
    font-family: "Cinzel", serif;
    font-weight: 400;
    color: var(--white);
    letter-spacing: 1px;
    display: flex; align-items: center; gap: 10px;
    position: absolute;
  }
  .brand-dot { width: 12px; height: 12px; border: 1.5px solid var(--white); border-radius: 50%; flex: none; }

  /* front */
  .card-front .brand { font-size: 26px; left: 0; right: 0; top: 78px; justify-content: center; }
  .contact-block {
    position: absolute; left: 46px; right: 30px; bottom: 46px;
    display: flex; align-items: center;
  }
  .person { text-align: right; padding-right: 22px; }
  .person-name { font-family: "Cinzel", serif; color: var(--blue); font-size: 24px; line-height: 1.1; }
  .person-role { font-size: 13px; color: var(--muted); margin-top: 6px; }
  .divider { width: 1px; height: 84px; background: #8a8a8a; }
  .contact-list { list-style: none; padding-left: 20px; font-size: 13px; line-height: 1.9; }
  .contact-list li { display: flex; align-items: center; gap: 8px; }
  .contact-list svg { width: 13px; height: 13px; fill: var(--red); flex: none; }

  /* back */
  .card-back .brand {
    font-size: 24px; line-height: 1.25;
    left: 32px; top: 50%; transform: translateY(-50%);
    width: 236px;
  }
  .brand-lines { display: flex; flex-direction: column; }
  .services { position: absolute; left: 292px; top: 34px; right: 18px; }
  .guarantee { color: var(--red); font-weight: 700; font-size: 13px; line-height: 1.2; text-transform: uppercase; }
  .special-band {
    background: var(--blue); color: var(--white); font-weight: 700; font-size: 12px;
    padding: 2px 8px; margin: 4px 0 8px; text-transform: uppercase;
    clip-path: polygon(0 0, 100% 0, 94% 100%, 0 100%);
  }
  .service-list { list-style: none; font-size: 12px; line-height: 1.55; font-weight: 600; }
  .service-list li { display: flex; align-items: center; gap: 6px; white-space: nowrap; }
  .service-list svg { width: 11px; height: 11px; flex: none; }
</style>
</head>
<body>
  <section class="card card-front">
    <div class="brand"><span class="brand-dot"></span>Harborline Renovations</div>
    <div class="contact-block">
      <div class="person">
        <div class="person-name">MARCUS DELL</div>
        <div class="person-role">Director</div>
      </div>
      <div class="divider"></div>
      <ul class="contact-list">
        <li><svg viewBox="0 0 24 24"><path d="M6.6 10.8a15 15 0 0 0 6.6 6.6l2.2-2.2c.3-.3.7-.4 1-.2 1.1.4 2.3.6 3.6.6.6 0 1 .4 1 1V20c0 .6-.4 1-1 1A17 17 0 0 1 3 4c0-.6.4-1 1-1h3.5c.6 0 1 .4 1 1 0 1.3.2 2.5.6 3.6.1.3 0 .7-.2 1z"/></svg>555-014-7390</li>
        <li><svg viewBox="0 0 24 24"><path d="M2 5h20v14H2z M3 6l9 7 9-7" stroke="#141414" stroke-width="1.5"/></svg>md@brightoakbuilders.example</li>
        <li><svg viewBox="0 0 24 24"><circle cx="12" cy="12" r="10"/><path d="M2 12h20M12 2v20M5 6h14M5 18h14" stroke="#141414" stroke-width="1.3" fill="none"/></svg>www.brightoakbuilders.example</li>
      </ul>
    </div>
  </section>

  <section class="card card-back">
    <div class="brand"><span class="brand-dot"></span><span class="brand-lines"><span>Harborline</span><span>Renovations</span></span></div>
    <div class="services">
      <div class="guarantee">Our services are<br>100% guaranteed</div>
      <div class="special-band">Specializing in:</div>
      <ul class="service-list">
        <li><svg viewBox="0 0 12 12"><rect x="1" y="3" width="8" height="8" fill="none" stroke="#e0232a" stroke-width="1.2"/><path d="M3 6l2 2 6-7" fill="none" stroke="#e0232a" stroke-width="1.6"/></svg>Remodel: Kitchen &amp; Bath</li>
        <li><svg viewBox="0 0 12 12"><rect x="1" y="3" width="8" height="8" fill="none" stroke="#e0232a" stroke-width="1.2"/><path d="M3 6l2 2 6-7" fill="none" stroke="#e0232a" stroke-width="1.6"/></svg>Painting: Interior &amp; Exterior</li>
        <li><svg viewBox="0 0 12 12"><rect x="1" y="3" width="8" height="8" fill="none" stroke="#e0232a" stroke-width="1.2"/><path d="M3 6l2 2 6-7" fill="none" stroke="#e0232a" stroke-width="1.6"/></svg>Flooring: Carpet, Vinyl, Wood</li>
        <li><svg viewBox="0 0 12 12"><rect x="1" y="3" width="8" height="8" fill="none" stroke="#e0232a" stroke-width="1.2"/><path d="M3 6l2 2 6-7" fill="none" stroke="#e0232a" stroke-width="1.6"/></svg>Window &amp; Door Replacement</li>
        <li><svg viewBox="0 0 12 12"><rect x="1" y="3" width="8" height="8" fill="none" stroke="#e0232a" stroke-width="1.2"/><path d="M3 6l2 2 6-7" fill="none" stroke="#e0232a" stroke-width="1.6"/></svg>Plumbing: Repairs &amp; Upgrades</li>
        <li><svg viewBox="0 0 12 12"><rect x="1" y="3" width="8" height="8" fill="none" stroke="#e0232a" stroke-width="1.2"/><path d="M3 6l2 2 6-7" fill="none" stroke="#e0232a" stroke-width="1.6"/></svg>Energy-Efficient Upgrades</li>
        <li><svg viewBox="0 0 12 12"><rect x="1" y="3" width="8" height="8" fill="none" stroke="#e0232a" stroke-width="1.2"/><path d="M3 6l2 2 6-7" fill="none" stroke="#e0232a" stroke-width="1.6"/></svg>Deck &amp; Patio Construction</li>
        <li><svg viewBox="0 0 12 12"><rect x="1" y="3" width="8" height="8" fill="none" stroke="#e0232a" stroke-width="1.2"/><path d="M3 6l2 2 6-7" fill="none" stroke="#e0232a" stroke-width="1.6"/></svg>Water &amp; Mold Damage</li>
        <li><svg viewBox="0 0 12 12"><rect x="1" y="3" width="8" height="8" fill="none" stroke="#e0232a" stroke-width="1.2"/><path d="M3 6l2 2 6-7" fill="none" stroke="#e0232a" stroke-width="1.6"/></svg>Garage Renovation</li>
      </ul>
    </div>
  </section>
</body>
</html>
```